RivoCounsel Compensation Lawyers

We need a modern, sleek letterhead that is professional.

In relation to the footer, we would like to have firm contact details there ideally, however you must also insert at the bottom of each page the following....

Liability limited by a scheme approved under the Professional Standards Legislation.

From the attachment you can extract the firm logo. Also, I would like the Accredited specialist circle on the letterhead also.

Also, I would like you to create a document that can easily be edited for change of contact details, as these are likely to change.

Industry/Entity Type

It Professional

Font styles to use
Sans Serif

Colors
0655a3
3276b5
85abd2
0492cd
33a6d7
85cae6
cee9f5
eaf1f7
cbcbcb

Requirements
Must have
• Ph: 8371-5264
• F: 8815-3927
• M 0468-253-914
• mk@rivocounsel.example.au
• www.rivocounsel.example.au
Nice to have
• the word document gives you an idea of what I like. I am happy for your to amaze me with your creativity.

```html
<!DOCTYPE html>
<html lang="en">
<head>
<meta charset="utf-8">
<title>RivoCounsel Compensation Lawyers – Letterhead</title>
<link rel="stylesheet" href="https://fonts.googleapis.com/css2?family=Roboto+Condensed:wght@400&family=PT+Sans:wght@400&display=swap">
<style>
  :root {
    --navy: #0655a3;
    --blue: #3276b5;
    --sky: #0492cd;
    --sky-light: #33a6d7;
    --pale: #cee9f5;
    --mist: #eaf1f7;
    --rule: #cbcbcb;
    --ink-grey: #6b6b6b;
    --backdrop: #e6e6e6;
    --paper: #ffffff;
  }
  * { margin: 0; padding: 0; box-sizing: border-box; }
  html, body {
    width: 1145px; height: 1200px; overflow: hidden;
    background: var(--backdrop);
    font-family: "PT Sans", Arial, sans-serif;
  }
  .letterhead {
    position: absolute; left: 235px; top: 124px;
    width: 674px; height: 952px;
    background: var(--paper);
    overflow: hidden;
  }
  .brand-mark {
    position: absolute; left: 30px; top: 31px;
    width: 58px; height: 58px; border-radius: 50%;
    background: var(--sky-light);
  }
  .brand-name {
    position: absolute; left: 113px; top: 37px;
    font-family: "Roboto Condensed", "Arial Narrow", sans-serif;
    font-size: 21px; font-weight: 400; color: var(--navy);
    white-space: nowrap;
  }
  .brand-url {
    position: absolute; left: 113px; top: 61px;
    font-size: 11.5px; letter-spacing: 0.4px; color: var(--sky);
  }
  .contact {
    position: absolute; right: 25px; top: 27px;
    text-align: right; list-style: none;
    font-size: 9.5px; line-height: 12.3px; color: var(--ink-grey);
  }
  .header-rule {
    position: absolute; left: 20px; right: 23px; top: 106px;
    border-top: 1px solid var(--rule);
  }
  .accreditation-badge {
    position: absolute; left: 23px; top: 873px;
    width: 46px; height: 46px; border-radius: 50%;
    border: 2px solid var(--rule); background: var(--mist);
  }
  .practice-areas {
    position: absolute; left: 80px; top: 880px;
    font-size: 12.5px; color: var(--navy); white-space: nowrap;
    letter-spacing: 0.1px;
  }
  .practice-areas .sep { margin: 0 5px; }
  .liability-note {
    position: absolute; left: 80px; top: 900px;
    font-size: 8.5px; color: var(--ink-grey);
  }
  .footer-band {
    position: absolute; left: 0; right: 0; bottom: 0;
    height: 7px; background: var(--navy);
  }
</style>
</head>
<body>
  <main class="letterhead">
    <header>
      <span class="brand-mark"></span>
      <h1 class="brand-name">RivoCounsel Compensation Lawyers</h1>
      <p class="brand-url">www.rivocounsel.example.au</p>
      <ul class="contact">
        <li>Ph: 8371-5264</li>
        <li>F: 8815-3927</li>
        <li>M 0468-253-914</li>
        <li>mk@rivocounsel.example.au</li>
      </ul>
      <div class="header-rule"></div>
    </header>

    <footer>
      <span class="accreditation-badge"></span>
      <p class="practice-areas">INSURANCE LAW<span class="sep">|</span>ESTATE &amp; PROPERTY LAW<span class="sep">|</span>FAMILY LAW<span class="sep">|</span>COMMERCIAL LAW</p>
      <p class="liability-note">Liability limited by a scheme approved under the Professional Standards Legislation.</p>
      <div class="footer-band"></div>
    </footer>
  </main>
</body>
</html>
```